Invitation card to the opening of BRAVORA FITNESS CLUB

A successful training plan starts with BRAVORA Fitness!
Join us for our grand opening! OPEN HOUSE AND YOU ARE INVITED!
Tuesday 1st of August, 2017
Classes start from 7.30am till 9.30pm.
Explore the most fun, exciting, challenging and effective training system in the region.
Healthy drinks and delicious food will be provided.
We hope to see you there!

www.bravorafitnessclub.example
APP: BRAVORAFITQZN
Tel: 81-42 09 15

Industry/Entity Type

Fitness

Colors

Designer to choose colors to be used in the design.

Requirements
Must have
• Elegant card
Nice to have
• Logo in the background
Should not have
• pictures

```html
<!DOCTYPE html>
<html lang="en">
<head>
<meta charset="utf-8">
<title>Bravora Fitness Club – Grand Opening Invitation</title>
<link rel="stylesheet" href="https://fonts.googleapis.com/css2?family=Archivo:wght@800;900&family=Arimo:wght@400;700&family=Roboto+Condensed:wght@400;700&family=Playball&display=swap">
<style>
  :root {
    --page-bg: #e6e4e0;
    --slate: #6e8b9b;
    --slate-deep: #5f7c8d;
    --navy: #173f5c;
    --white: #ffffff;
    --gold-dark: #b0822a;
    --gold-mid: #d9b25a;
    --gold-light: #fff2b8;
  }
  * { box-sizing: border-box; margin: 0; padding: 0; }
  html, body {
    width: 1200px; height: 750px; overflow: hidden;
    background: var(--page-bg);
  }
  .canvas {
    position: relative; width: 1200px; height: 750px; overflow: hidden;
  }
  .invitation-frame {
    position: absolute; left: 343px; top: 15px;
    width: 514px; height: 720px; overflow: hidden;
    box-shadow: 0 6px 18px rgba(0,0,0,.18);
  }
  .invitation {
    position: absolute; left: 0; top: 0;
    width: 580px; height: 813px;
    transform: scale(0.8856); transform-origin: 0 0;
    font-family: "Arimo", Arial, sans-serif;
    color: var(--navy);
  }
  .invitation__backdrop {
    position: absolute; inset: 0;
    background: radial-gradient(ellipse at 50% 35%, var(--slate) 0%, var(--slate-deep) 100%);
  }
  .brand {
    position: absolute; left: 0; top: 22px; width: 100%;
    text-align: center; color: var(--white);
    font-family: "Arimo", Arial, sans-serif; font-weight: 400;
  }
  .brand__mark {
    display: block; margin: 0 auto 14px;
    width: 118px; height: 118px; border-radius: 50%;
    border: 6px solid #d8dde0;
  }
  .brand__name { display: block; font-size: 58px; letter-spacing: 2px; line-height: 1; }
  .brand__sub { display: block; margin-top: 10px; font-size: 22px; letter-spacing: 10px; line-height: 1; }

  .headline-band {
    position: absolute; left: 0; top: 268px; width: 100%; height: 148px;
    background: linear-gradient(100deg, var(--gold-dark) 0%, var(--gold-mid) 25%, var(--gold-light) 50%, var(--gold-mid) 75%, var(--gold-dark) 100%);
    text-align: center; font-family: "Archivo", Arial, sans-serif; font-weight: 900;
    text-transform: uppercase; line-height: 1;
  }
  .headline-band__top { display: block; margin-top: 18px; font-size: 41px; letter-spacing: -0.5px; color: var(--navy); }
  .headline-band__mid { display: block; margin-top: 6px; font-family: "Arimo", Arial, sans-serif; font-weight: 400; font-size: 30px; color: #111; transform: scaleY(1.1); }
  .headline-band__bottom { display: block; margin-top: 8px; font-size: 41px; letter-spacing: -0.5px; color: var(--navy); }

  .invite-lines {
    position: absolute; left: 0; top: 430px; width: 100%;
    text-align: center; font-weight: 700; font-size: 22px; line-height: 32px;
  }
  .event-date {
    position: absolute; left: 0; top: 498px; width: 100%;
    text-align: center; font-family: "Playball", cursive; font-size: 46px;
    color: var(--gold-mid); text-shadow: 2px 2px 0 #2a2a2a;
  }
  .event-date__year { font-family: "Arimo", Arial, sans-serif; font-weight: 700; font-size: 42px; }

  .gold-rule {
    position: absolute; left: 0; height: 4px;
    background: linear-gradient(90deg, var(--gold-dark), var(--gold-light) 50%, var(--gold-dark));
  }
  .gold-rule--full { top: 568px; width: 100%; }
  .gold-rule--left { top: 705px; width: 165px; }
  .gold-rule--right { top: 705px; left: 415px; width: 165px; }

  .details {
    position: absolute; left: 0; width: 100%; text-align: center;
    font-family: "Roboto Condensed", Arial, sans-serif; font-size: 18.5px;
    line-height: 21px; text-transform: uppercase;
  }
  .details--explore { top: 588px; }
  .details--food { top: 643px; }
  .closing {
    position: absolute; left: 0; top: 696px; width: 100%; text-align: center;
    font-weight: 700; font-size: 16px; text-transform: uppercase;
  }
  .contacts {
    position: absolute; left: 0; top: 752px; width: 100%; text-align: center;
    font-size: 15px; line-height: 24px;
  }
  .contacts__row { padding-right: 20px; }
  .contacts__sep { margin: 0 6px; }

  .hours-badge {
    position: absolute; left: 418px; top: 665px; width: 140px; height: 140px;
  }
  .hours-badge svg { position: absolute; inset: 0; width: 100%; height: 100%; }
  .hours-badge__text {
    position: absolute; inset: 0; display: flex; flex-direction: column;
    align-items: center; justify-content: center;
    transform: rotate(-22deg); color: #111;
    font-weight: 700; font-size: 14px; line-height: 16px; text-align: center;
  }
  .hours-badge__time { font-size: 21px; line-height: 22px; }
</style>
</head>
<body>
<main class="canvas">
  <article class="invitation-frame">
    <div class="invitation">
      <div class="invitation__backdrop" role="img" aria-label="Slate blue background with a faint tone-on-tone floral swirl pattern"></div>

      <header class="brand">
        <span class="brand__mark"></span>
        <span class="brand__name">BRAVORA</span>
        <span class="brand__sub">FITNESS</span>
      </header>

      <h1 class="headline-band">
        <span class="headline-band__top">Successful Training</span>
        <span class="headline-band__mid">Plan Starts With</span>
        <span class="headline-band__bottom">Bravora Fitness!</span>
      </h1>

      <p class="invite-lines">Join Us For Our Grand Opening!<br>Open House And You Are Invited!</p>

      <p class="event-date">Tuesday 1st of August, <span class="event-date__year">2017</span></p>

      <div class="gold-rule gold-rule--full"></div>

      <p class="details details--explore">Explore the most fun, exciting, challenging<br>and effective training system in the region.</p>
      <p class="details details--food">Healthy drinks and delicious food<br>will be provided.</p>

      <div class="gold-rule gold-rule--left"></div>
      <p class="closing">We hope to see you there!</p>
      <div class="gold-rule gold-rule--right"></div>

      <footer class="contacts">
        <div class="contacts__row">bravorafitqzn <span class="contacts__sep">|</span>81-42 09 15</div>
        <div class="contacts__row">www.bravorafitnessclub.example</div>
      </footer>

      <div class="hours-badge">
        <svg viewBox="0 0 130 130" aria-hidden="true">
          <defs>
            <radialGradient id="badgeGold" cx="40%" cy="35%" r="70%">
              <stop offset="0" stop-color="#fff2b8"/>
              <stop offset="0.55" stop-color="#d9b25a"/>
              <stop offset="1" stop-color="#a57a25"/>
            </radialGradient>
          </defs>
          <polygon fill="url(#badgeGold)" points="129,65 119.3,73.6 125.9,84.8 114,90 116.8,102.6 103.9,103.9 102.6,116.8 90,114 84.8,125.9 73.6,119.3 65,129 56.4,119.3 45.2,125.9 40,114 27.4,116.8 26.1,103.9 13.2,102.6 16,90 4.1,84.8 10.7,73.6 1,65 10.7,56.4 4.1,45.2 16,40 13.2,27.4 26.1,26.1 27.4,13.2 40,16 45.2,4.1 56.4,10.7 65,1 73.6,10.7 84.8,4.1 90,16 102.6,13.2 103.9,26.1 116.8,27.4 114,40 125.9,45.2 119.3,56.4"/>
        </svg>
        <p class="hours-badge__text">
          <span>Classes start</span>
          <span>from</span>
          <span class="hours-badge__time">7.30am</span>
          <span>till</span>
          <span class="hours-badge__time">9.30pm</span>
        </p>
      </div>
    </div>
  </article>
</main>
</body>
</html>
```